Counseling Practice Business Card

I need a professional looking business card incorporating my new logo that was just completed. Card needs to incorporate my name and title, description of my specialty, my address, my phone number, my fax number, my email and my website URL. I need to be able to choose design on/with different paper colors and textures.
I do not have a lot of business card ideas so I am open to anything but I want bold,sharp, clear card without additional designs other than my logo (see attached file info). I am open to different color backgrounds or paper colors including black. I do not like traditional brackets around area codes in phone number or dashes between numbers in phone number. Am open to other ways of presenting including periods between numbers as appropriate. I do not know enough to know what I like yet but I want card to coordinate and work together with my logo. My practice emphasizes natural mental health interventions so any use of color (with background paper color or the blue and green in my logo) that elicits nature is nice. In addition to black, any natural brown or wood looking background might be desirable also. Most of the offerings so far look very similar and boring.

Target Market(s)

Potential therapy clients and other professionals

Contact Information for Business Card

Card information:
Marcus T. Whitfield, Ph.D.
Licensed Clinical Psychologist
Integrative Health Coach
4812 Ferndale Pkwy NW
Suite 730
Duluth, GA 30096
(770) 555-0142 phone
(770) 555-0186 fax
drmarcuswhitfield@kelvora.com
pathbloomcounseling.com

Font styles to use
Serif
Sans Serif
Other font styles liked:
• anything that you think looks crisp, clear and easily readable

Requirements
Must have
• Any color used should coordinate with my logo design (see attached files).
• Card should be printed horizontally so top and bottom are longest sides of rectangle.
• Background color or paper color should complement and highlight logo. Do not like a white background. black, grey, brown or any color my logo would blend well with.
Nice to have
• I would like designer to utilize color to highlight letters/name or phone-fax-web symbols.
• Bottom edge of card could be highlighted if appropriate to an idea.
Should not have
• I would NOT want the card to have a pure white background at all.
• No clear cards.
• Cards should be oriented with long sides on bottom and top, NOT sides. DO NOT LIKE THIS THIN TALL ORIENTATION.

```html
<!DOCTYPE html>
<html lang="en">
<head>
<meta charset="utf-8">
<title>Pathbloom Counseling – Business Card</title>
<link href="https://fonts.googleapis.com/css2?family=Montserrat:wght@400;500;600&display=swap" rel="stylesheet">
<style>
  :root {
    --backdrop: #2a2a2b;
    --card: #2b2826;
    --card-edge: #34302d;
    --blue: #3a8fd6;
    --green: #2fa35a;
    --text-light: #d9d6d2;
    --text-muted: #c9c5c0;
  }
  * { box-sizing: border-box; margin: 0; padding: 0; }
  html, body {
    width: 1200px; height: 900px; overflow: hidden;
    background: var(--backdrop);
    font-family: "Montserrat", sans-serif;
  }
  .stage {
    width: 1200px; height: 900px;
    display: flex; flex-direction: column; align-items: center; justify-content: center; gap: 40px;
  }
  .card {
    width: 700px; height: 400px;
    background: radial-gradient(circle at 50% 45%, var(--card-edge), var(--card) 70%);
    border-radius: 20px;
    box-shadow: 0 18px 40px rgba(0,0,0,.55);
    color: var(--text-light);
    position: relative;
  }
  .brand {
    font-weight: 600; color: var(--blue);
    display: inline-flex; align-items: center; gap: 12px;
    line-height: 1.1; white-space: nowrap;
  }
  .brand-dot {
    width: 14px; height: 14px; border-radius: 50%;
    background: var(--green); flex: none;
  }
  /* front */
  .card-front {
    display: flex; flex-direction: column; align-items: center; justify-content: center;
    text-align: center;
  }
  .card-front .brand { font-size: 40px; }
  .front-url {
    margin-top: 20px; font-size: 18px; font-weight: 600; color: var(--green);
  }
  /* back */
  .card-back {
    display: grid; grid-template-columns: 1fr 1fr; align-items: center;
    padding: 40px 48px;
  }
  .identity { display: flex; flex-direction: column; align-items: flex-start; }
  .holder-name {
    font-size: 18px; font-weight: 600; color: var(--blue); text-transform: uppercase;
    letter-spacing: .02em; white-space: nowrap;
  }
  .holder-title { font-size: 14px; color: var(--text-muted); margin-top: 6px; line-height: 1.45; }
  .rule { width: 24px; height: 3px; background: var(--blue); margin: 18px 0; }
  .card-back .brand { font-size: 24px; gap: 10px; }
  .card-back .brand-dot { width: 12px; height: 12px; }
  .address {
    margin-top: 18px; font-size: 14px; line-height: 1.6; color: var(--text-muted);
    font-style: normal;
  }
  .contacts { list-style: none; padding-left: 28px; border-left: 1px solid rgba(255,255,255,.08); }
  .contact {
    display: flex; align-items: center; gap: 12px;
    font-size: 14px; color: var(--text-muted); white-space: nowrap;
  }
  .contact + .contact { margin-top: 18px; }
  .contact-icon {
    width: 24px; height: 24px; border-radius: 50%; background: var(--blue);
    display: flex; align-items: center; justify-content: center; flex: none;
  }
  .contact-icon svg { width: 13px; height: 13px; }
  .web-accent { color: var(--blue); }
  .edge-band {
    position: absolute; left: 0; right: 0; bottom: 0; height: 6px;
    background: linear-gradient(90deg, var(--green), var(--blue));
    border-radius: 0 0 20px 20px;
  }
</style>
</head>
<body>
<main class="stage">
  <section class="card card-front">
    <div class="brand"><span class="brand-dot"></span><span>Pathbloom Counseling</span></div>
    <p class="front-url">www.pathbloomcounseling.com</p>
  </section>

  <section class="card card-back">
    <div class="identity">
      <h1 class="holder-name">Marcus T. Whitfield, Ph.D.</h1>
      <p class="holder-title">Licensed Clinical Psychologist<br>Integrative Health Coach</p>
      <div class="rule"></div>
      <div class="brand"><span class="brand-dot"></span><span>Pathbloom Counseling</span></div>
      <address class="address">4812 Ferndale Pkwy NW<br>Suite 730<br>Duluth, GA 30096</address>
    </div>
    <ul class="contacts">
      <li class="contact">
        <span class="contact-icon"><svg viewBox="0 0 16 16"><path fill="#fff" d="M3.6 1.5l2.2 2.6-1.3 1.6c.9 2 2.4 3.5 4.4 4.4l1.6-1.3 2.6 2.2-1.2 2.3C7 13.2 2.8 9 2 3.2z"/></svg></span>
        770.555.0142
      </li>
      <li class="contact">
        <span class="contact-icon"><svg viewBox="0 0 16 16"><rect x="4" y="2" width="8" height="4" fill="#fff"/><rect x="2" y="6" width="12" height="6" rx="1" fill="#fff"/><rect x="4.5" y="10" width="7" height="4" fill="#3a8fd6" stroke="#fff" stroke-width="1"/></svg></span>
        770.555.0186
      </li>
      <li class="contact">
        <span class="contact-icon"><svg viewBox="0 0 16 16"><rect x="2" y="4" width="12" height="8" fill="#fff"/><path d="M2 4l6 5 6-5" fill="none" stroke="#3a8fd6" stroke-width="1.3"/></svg></span>
        drmarcuswhitfield@kelvora.com
      </li>
      <li class="contact">
        <span class="contact-icon"><svg viewBox="0 0 16 16"><circle cx="8" cy="8" r="5.5" fill="none" stroke="#fff" stroke-width="1.4"/><path d="M2.5 8h11M8 2.5c-2.5 3-2.5 8 0 11M8 2.5c2.5 3 2.5 8 0 11" fill="none" stroke="#fff" stroke-width="1.1"/></svg></span>
        <span>www.<span class="web-accent">pathbloomcounseling</span>.com</span>
      </li>
    </ul>
    <div class="edge-band"></div>
  </section>
</main>
</body>
</html>
```